Information Management & Advanced Analytics Company Needs a Web Design

We need a web design for a new company based in Singapore called Velmoric Solutions. We provides information management and advanced analytics services and solutions across a wide variety of industries (Financial Services, Government and Public Sector, Oil & Gas among others). We are not like any other System Integrator, as we believe in bringing together the science and art of data (and data science) to our clients. Science in the sense of understanding technology and Art in the sense of how to operationalise across a culture/people/processes. As with the name of the company Velmoric, which is a play on the words 'Ascending', we want a final design should communicate growth and our ability to help an organisation ascend towards better outcomes.

We have put some very high level ideas in a document however happy to leave an open hand for ideas and recommendation on design. Content can be incorporated/updated moving forwards.

To clarify on the scope of the work (thanks for the feedback); it is to create a framework for 5 pages (1 is comprehensive - services, while 2 are purely information to public, such as about us and contact us and finally join us and partners may have some dynamic information that will be updated). We would like to create a simple, yet elegant site that is intuitive and communicates progression and growth. We are open to ideas on design hence trying to first focus on look/feel/flow and then fill up with detailed content. Thanks.

Note that 'Join Us' is for hiring purposes (open positions and submission of CVs).

1. Possible to request for a more Asian look.
2. You may want to take a look at this site, www.pordlex.example, website designs are moving towards this manner to support different devices and platforms.
Updates

Hi all,1. Possible to request for a more Asian look especially the stock pictures that are used.2. Take a look at this site, www.pordlex.example, website designs are moving towards this manner to support different devices and platforms. More use of infographics too. Added Tuesday, October 6, 2015

Project Deadline Extended Reason: We would like a more Asian look given our operating location. Likewise, we would like designers to consider a design that will support different devices and platforms such as www.pordlex.example. As such we would like to provide more time. Thanks. Added Tuesday, October 6, 2015

Target Market(s)

We provide implementation and consultancy services to a wide range of industries. The audience/market would be those seeking for; 1. Revenue Enhancement, 2. Operations Optimisation, 3. Risk Management

Industry/Entity Type

Information Technology

Coding

Coded - Design and coding required

Number of Pages Required

5+ page

Font styles to use
Sans Serif

Requirements
Must have
• Other than the landing page we should have the following pages (in no particular order); Services, About Us, Contact Us, Join Us, Partners.
• Our main service areas and focus are
• - Information Management
• - Advanced Analytics
Nice to have
• Given our approach of art and science, it would be nice to have a design that captures that essence of combining technology with consultancy.
• Regarding colors, see the uploaded company logo for ideas of color schemes to use and align to.
Should not have
• The site should be accessible from handheld devices so drop down menus are not advisable as they do not always function on these devices.

```html
<!DOCTYPE html>
<html lang="en">
<head>
<meta charset="utf-8">
<title>Velmoric Solutions</title>
<link rel="stylesheet" href="https://fonts.googleapis.com/css2?family=Open+Sans:wght@400;600;700&family=Montserrat:wght@600;700&display=swap">
<style>
:root{
  --orange:#e2561f;
  --orange-dark:#c94814;
  --ink:#333333;
  --muted:#7a7a7a;
  --light:#f3f3f3;
  --line:#e3e3e3;
  --dark:#2c2c2e;
  --darker:#222224;
  --white:#ffffff;
}
*{box-sizing:border-box;margin:0;padding:0}
html,body{width:1200px;height:2624px;overflow:hidden}
body{font-family:"Open Sans",Arial,sans-serif;color:var(--ink);background:var(--white);font-size:12px;line-height:1.6}
.page{width:1200px;height:2624px;position:relative;overflow:hidden}
.wrap{width:1000px;margin:0 auto;position:relative}
h2.section-title{font-family:"Montserrat","Open Sans",sans-serif;font-size:17px;font-weight:700;text-align:center;letter-spacing:.5px;color:var(--ink)}
h2.section-title::after{content:"";display:block;width:44px;height:2px;background:var(--orange);margin:10px auto 0}
.intro{text-align:center;color:var(--muted);font-size:12px;width:760px;margin:14px auto 0}
.read-more{color:var(--orange);font-size:11px;font-weight:600;text-decoration:none}

/* header */
.site-header{height:72px;background:var(--white);border-bottom:1px solid var(--line)}
.site-header .wrap{display:flex;align-items:center;justify-content:space-between;height:72px}
.brand{display:flex;align-items:center;gap:10px}
.brand-mark{width:14px;height:14px;background:var(--orange);flex:none}
.brand-name{font-family:"Open Sans",sans-serif;font-size:22px;font-weight:600;color:var(--ink);line-height:1}
.main-nav{display:flex;height:72px}
.main-nav a{display:flex;align-items:center;padding:0 18px;font-size:10px;font-weight:700;color:var(--ink);text-decoration:none;letter-spacing:.5px}
.main-nav a.is-active{background:var(--orange);color:var(--white)}

/* hero */
.hero{height:520px;position:relative;overflow:hidden}
.hero-photo{position:absolute;inset:0;background:linear-gradient(100deg,#e9ecef 0%,#c7ccd3 35%,#6b7684 65%,#2f3945 100%)}
.hero-devices{position:absolute;left:640px;top:120px;width:300px;height:200px;background:linear-gradient(160deg,#ffffff,#d9dde2);border-radius:6px;box-shadow:0 8px 24px rgba(0,0,0,.25)}
.hero-copy{position:absolute;left:160px;top:150px;width:380px}
.hero-copy h1{font-family:"Montserrat",sans-serif;color:var(--orange);font-size:34px;font-weight:700}
.hero-copy p{color:#555;font-size:12px;margin:12px 0 22px}
.btn{display:inline-block;padding:9px 20px;font-size:10px;font-weight:700;color:var(--white);text-decoration:none;margin-right:8px;letter-spacing:.5px}
.btn-dark{background:var(--dark)}
.btn-orange{background:var(--orange)}
.hero-arrow{position:absolute;top:305px;width:30px;height:30px;border-radius:50%;background:rgba(255,255,255,.8);display:flex;align-items:center;justify-content:center}
.hero-arrow.prev{left:36px}.hero-arrow.next{right:36px}

/* services */
.services{padding:50px 0 0;height:410px}
.service-cards{display:flex;justify-content:center;gap:30px;margin-top:36px}
.service-card{width:290px;background:var(--white);box-shadow:0 4px 14px rgba(0,0,0,.12);text-align:center;padding:0 22px 18px;position:relative}
.service-icon{width:54px;height:54px;border-radius:50%;background:var(--orange);margin:-20px auto 10px;display:flex;align-items:center;justify-content:center;border:4px solid var(--white);box-shadow:0 0 0 1px var(--line)}
.service-card h3{font-size:13px;font-weight:700;margin-bottom:6px}
.service-card p{font-size:11px;color:var(--muted);margin-bottom:8px}

/* focus band */
.focus{height:450px;position:relative;margin-top:18px}
.focus-photo{position:absolute;inset:0;background:linear-gradient(180deg,#1d2230 0%,#2b3244 55%,#151821 100%)}
.focus .wrap{padding-top:26px}
.focus h2.section-title{color:var(--white)}
.focus-cards{display:flex;justify-content:center;gap:14px;margin-top:26px}
.focus-card{width:300px;background:var(--white)}
.focus-card .thumb{height:170px}
.focus-card .body{padding:12px 20px 16px;text-align:center}
.focus-card h3{font-size:12px;font-weight:700;margin-bottom:4px}
.focus-card p{font-size:10.5px;color:var(--muted);margin-bottom:6px}

/* who & how */
.approach{height:320px;padding-top:28px}
.approach .wrap{display:flex;gap:40px}
.approach-col{flex:1}
.approach-col h2{font-family:"Montserrat",sans-serif;font-size:14px;font-weight:700;margin-bottom:18px}
.approach-col h2::after{content:"";display:block;width:36px;height:2px;background:var(--orange);margin-top:8px}
.approach-body{display:flex;gap:18px}
.approach-body .thumb{width:200px;height:150px;flex:none}
.approach-body p{font-size:11px;color:var(--muted);margin-bottom:8px}

/* about */
.about{background:var(--light);height:390px;padding-top:36px}
.team{display:flex;justify-content:center;gap:70px;margin-top:30px}
.member{width:170px;text-align:center}
.member .portrait{width:100px;height:100px;border-radius:50%;margin:0 auto 12px;border:4px solid var(--white);background:linear-gradient(160deg,#d8cfc6,#8e8078)}
.member h4{color:var(--orange);font-size:11px;font-weight:700}
.member p{font-size:10.5px;color:var(--muted)}

/* partners */
.partners{height:190px;padding-top:34px}
.partner-row{display:flex;align-items:center;justify-content:center;gap:44px;margin-top:34px}
.partner-badge{width:110px;height:30px;background:#c9c9c9;border-radius:4px}
.partner-arrow{width:20px;height:20px}

/* footer */
.site-footer{background:var(--dark);height:244px;color:#bdbdbd;position:relative}
.site-footer .wrap{display:flex;gap:46px;padding-top:30px}
.footer-col h5{color:var(--white);font-size:11px;font-weight:700;letter-spacing:.5px;margin-bottom:12px}
.footer-about{width:230px;font-size:10.5px}
.footer-about .brand-name{font-size:20px;color:var(--white)}
.footer-about p{margin-top:14px}
.footer-links{width:140px}
.footer-links li{list-style:none;font-size:10.5px;line-height:1.9}
.footer-map{width:200px}
.footer-map .map{width:180px;height:110px;background:linear-gradient(135deg,#e8e6df,#cfd6cf)}
.footer-contact{width:240px;font-size:10.5px}
.footer-contact li{list-style:none;display:flex;gap:10px;margin-bottom:9px;align-items:flex-start}
.footer-contact .dot{width:18px;height:18px;border-radius:50%;background:var(--orange);flex:none;display:flex;align-items:center;justify-content:center}
.social{display:flex;gap:6px;margin-top:8px}
.social span{width:20px;height:20px;border-radius:50%;border:1px solid #8a8a8a}
.footer-bar{position:absolute;bottom:0;left:0;right:0;height:36px;background:var(--darker);font-size:10px;display:flex;align-items:center}
.footer-bar .wrap{display:block;padding:0}
</style>
</head>
<body>
<div class="page">

<header class="site-header">
  <div class="wrap">
    <div class="brand"><span class="brand-mark"></span><span class="brand-name">Velmoric</span></div>
    <nav class="main-nav">
      <a href="#" class="is-active">HOME</a><a href="#">SERVICES</a><a href="#">ABOUT US</a><a href="#">CONTACT US</a><a href="#">JOIN US</a><a href="#">PARTNERS</a>
    </nav>
  </div>
</header>

<section class="hero">
  <div class="hero-photo" role="img" aria-label="Photo of business colleagues reviewing data at an office desk"></div>
  <div class="hero-devices" role="img" aria-label="Illustration of the website shown on desktop, tablet and phone"></div>
  <div class="hero-copy">
    <h1>Velmoric Solutions</h1>
    <p>We bring together the science and art of data, helping organisations across every industry turn information into better outcomes.</p>
    <a href="#" class="btn btn-dark">JOIN US</a><a href="#" class="btn btn-orange">READ MORE</a>
  </div>
  <span class="hero-arrow prev"><svg width="10" height="10" viewBox="0 0 10 10"><path d="M7 1 3 5l4 4" stroke="#333" stroke-width="1.6" fill="none"/></svg></span>
  <span class="hero-arrow next"><svg width="10" height="10" viewBox="0 0 10 10"><path d="M3 1l4 4-4 4" stroke="#333" stroke-width="1.6" fill="none"/></svg></span>
</section>

<section class="services">
  <div class="wrap">
    <h2 class="section-title">OUR SERVICE AREAS AND FOCUS</h2>
    <p class="intro">We provide information management and advanced analytics services to clients in financial services, government and the public sector, oil and gas and many more industries, combining technology with consultancy.</p>
    <div class="service-cards">
      <article class="service-card">
        <div class="service-icon"><svg width="22" height="22" viewBox="0 0 22 22"><rect x="4" y="3" width="14" height="16" rx="1" fill="none" stroke="#fff" stroke-width="2"/><path d="M7 8h8M7 11h8M7 14h5" stroke="#fff" stroke-width="1.6"/></svg></div>
        <h3>Information Management</h3>
        <p>Structured, governed and trusted data that supports every decision across your organisation.</p>
        <a href="#" class="read-more">Read More</a>
      </article>
      <article class="service-card">
        <div class="service-icon"><svg width="22" height="22" viewBox="0 0 22 22"><path d="M4 18V12M9 18V7M14 18v-8M19 18V4" stroke="#fff" stroke-width="2.4"/></svg></div>
        <h3>Analytics</h3>
        <p>Advanced models and insight that reveal patterns, forecast change and guide action.</p>
        <a href="#" class="read-more">Read More</a>
      </article>
      <article class="service-card">
        <div class="service-icon"><svg width="22" height="22" viewBox="0 0 22 22"><circle cx="11" cy="11" r="8" fill="none" stroke="#fff" stroke-width="2"/><circle cx="11" cy="11" r="4" fill="none" stroke="#fff" stroke-width="2"/><circle cx="11" cy="11" r="1.4" fill="#fff"/></svg></div>
        <h3>Organisation Transformation</h3>
        <p>Operationalising data across culture, people and processes so change truly lasts.</p>
        <a href="#" class="read-more">Read More</a>
      </article>
    </div>
  </div>
</section>

<section class="focus">
  <div class="focus-photo" role="img" aria-label="Photo of a city skyline at dusk"></div>
  <div class="wrap">
    <h2 class="section-title">WHAT I AM LOOKING FOR</h2>
    <div class="focus-cards">
      <article class="focus-card">
        <div class="thumb" role="img" aria-label="Photo of hands working with charts and a tablet" style="background:linear-gradient(135deg,#c9b7a0,#6d6a64)"></div>
        <div class="body"><h3>Revenue Enhancement</h3><p>Find new growth by understanding customers and markets through data.</p><a href="#" class="read-more">Read More</a></div>
      </article>
      <article class="focus-card">
        <div class="thumb" role="img" aria-label="Photo of a team planning around a desk with devices" style="background:linear-gradient(135deg,#d6cbb8,#7f6f5c)"></div>
        <div class="body"><h3>Operations Optimisation</h3><p>Streamline processes and reduce cost with clear operational insight.</p><a href="#" class="read-more">Read More</a></div>
      </article>
      <article class="focus-card">
        <div class="thumb" role="img" aria-label="Photo of a businessman looking over a city from a rooftop" style="background:linear-gradient(180deg,#cfd5db,#6f7780)"></div>
        <div class="body"><h3>Risk Management</h3><p>Anticipate, measure and control risk with reliable analytics.</p><a href="#" class="read-more">Read More</a></div>
      </article>
    </div>
  </div>
</section>

<section class="approach">
  <div class="wrap">
    <div class="approach-col">
      <h2>WHO WE ARE</h2>
      <div class="approach-body">
        <div class="thumb" role="img" aria-label="Photo of a waterfront skyline at night" style="background:linear-gradient(180deg,#2f4a78,#c98a4a)"></div>
        <div><p>We are a Singapore based team of data specialists who believe in uniting technology with a deep understanding of people.</p><p>Our consultants help clients ascend towards better outcomes, project after project.</p><a href="#" class="read-more">Read More</a></div>
      </div>
    </div>
    <div class="approach-col">
      <h2>HOW WE APPROACH DATA</h2>
      <div class="approach-body">
        <div class="thumb" role="img" aria-label="Photo of a calculator and financial reports on a desk" style="background:linear-gradient(135deg,#e4e4e4,#7c7c7c)"></div>
        <div><p>Science in understanding technology, art in how it is adopted across culture, people and processes.</p><p>This balance lets every solution deliver measurable and lasting value.</p><a href="#" class="read-more">Read More</a></div>
      </div>
    </div>
  </div>
</section>

<section class="about">
  <div class="wrap">
    <h2 class="section-title">ABOUT US</h2>
    <p class="intro">Our people bring years of experience in information management, analytics and consulting, working closely with clients to grow capability from within.</p>
    <div class="team">
      <div class="member"><div class="portrait" role="img" aria-label="Portrait photo of a team member"></div><h4>JOHN DOE</h4><p>Managing Director leading strategy and client partnerships.</p></div>
      <div class="member"><div class="portrait" role="img" aria-label="Portrait photo of a team member"></div><h4>JOHN DOE</h4><p>Head of Analytics building models and insight teams.</p></div>
      <div class="member"><div class="portrait" role="img" aria-label="Portrait photo of a team member"></div><h4>JOHN DOE</h4><p>Data Architect shaping platforms and governance.</p></div>
      <div class="member"><div class="portrait" role="img" aria-label="Portrait photo of a team member"></div><h4>JOHN DOE</h4><p>Principal Consultant guiding change and adoption.</p></div>
    </div>
  </div>
</section>

<section class="partners">
  <div class="wrap">
    <h2 class="section-title">OUR PARTNERS</h2>
    <div class="partner-row">
      <svg class="partner-arrow" viewBox="0 0 20 20"><path d="M13 4 7 10l6 6" stroke="#aaa" stroke-width="2" fill="none"/></svg>
      <span class="partner-badge"></span><span class="partner-badge"></span><span class="partner-badge"></span><span class="partner-badge"></span><span class="partner-badge"></span><span class="partner-badge"></span>
      <svg class="partner-arrow" viewBox="0 0 20 20"><path d="M7 4l6 6-6 6" stroke="#aaa" stroke-width="2" fill="none"/></svg>
    </div>
  </div>
</section>

<footer class="site-footer">
  <div class="wrap">
    <div class="footer-col footer-about">
      <div class="brand"><span class="brand-mark"></span><span class="brand-name">Velmoric</span></div>
      <p>Information management and advanced analytics services for organisations across Asia and beyond.</p>
    </div>
    <div class="footer-col footer-links">
      <h5>QUICK LINKS</h5>
      <ul><li>Home</li><li>Services</li><li>About Us</li><li>Contact Us</li><li>Join Us</li><li>Partners</li></ul>
    </div>
    <div class="footer-col footer-map">
      <h5>CONTACT US</h5>
      <div class="map" role="img" aria-label="Map showing the office location"></div>
    </div>
    <div class="footer-col footer-contact">
      <h5>WHERE TO FIND US</h5>
      <ul>
        <li><span class="dot"><svg width="9" height="11" viewBox="0 0 9 11"><path d="M4.5 10.5S1 6.5 1 4.2a3.5 3.5 0 0 1 7 0c0 2.3-3.5 6.3-3.5 6.3z" fill="#fff"/></svg></span><span>18 Harbour Lane, #05-02, Singapore 049100</span></li>
        <li><span class="dot"><svg width="10" height="10" viewBox="0 0 10 10"><path d="M2 1h2l1 2.5-1.2 1a5 5 0 0 0 2.7 2.7l1-1.2L10 7v2a1 1 0 0 1-1 1A8 8 0 0 1 0 2a1 1 0 0 1 1-1z" fill="#fff"/></svg></span><span>+65 6100 2000</span></li>
        <li><span class="dot"><svg width="10" height="8" viewBox="0 0 10 8"><rect x=".5" y=".5" width="9" height="7" fill="none" stroke="#fff"/><path d="M.5.5 5 4.5 9.5.5" stroke="#fff" fill="none"/></svg></span><span>hello@velmoric.example</span></li>
      </ul>
      <div class="social"><span></span><span></span><span></span><span></span><span></span></div>
    </div>
  </div>
  <div class="footer-bar"><div class="wrap">Copyright © 2015. All Rights Reserved Velmoric Solutions</div></div>
</footer>

</div>
</body>
</html>
```